HVAC company business card design

We need a business card design for a HVAC company. The design must look professional. Both sides will be used. The total data to be on the business card is
Name
Position
Email
Direct Phone/Moile Phone
Company Contacts /Address, Phone, Fax, web)
All data will be submit once the design is confirmed. For generic purposes use;
Emre Toksoy
Managing Director
+902324815263 (Mobile)
4712 Sokak No: 9 KBSE Yenikent IZMIR TURKEY
Tel: +902324815263 Fax : +902324815269
www.luvon.com.tr

Target Market(s)

HVAC

Industry/Entity Type

Business

Contact Information for Business Card

The total data to be on the business card is
Name
Position
Email
Direct Phone/Moile Phone
Emre Toksoy
Managing Director
+902324815263 (Mobile)
www.luvon.com.tr
The BC will use both sides of the card. The front will include the full logo and the details for the business card holder. The business card can be divided into vertical/horizontal or to a special shape. The common data like the company address/phone/fax should be indicated elsewehere. The back can contain some part or the whole logo and must contain the web address.

Font styles to use
Serif
Sans Serif

Colors
0355a3
cfdfed

Requirements
Should not have
• Please be careful with the fonts, it shouldnt be too small or too big and must not interfere with the logo fonts. If you need to use a curvy shape please do not use as the logo is already curvy or use the curves from the logo (if it looks good, otherwise forget it)
• We are not in favor of pictograms, only if they are perfect use them.

```html
<!DOCTYPE html>
<html lang="en">
<head>
<meta charset="utf-8">
<title>Luvon business card</title>
<link href="https://fonts.googleapis.com/css2?family=Open+Sans:wght@400;600;700&display=swap" rel="stylesheet">
<style>
  :root {
    --page: #eef2f6;
    --brand-blue: #0355a3;
    --brand-mid: #3a7fd0;
    --brand-light: #4fb6ea;
    --brand-pale: #cfdfed;
    --navy: #2a3a5c;
    --divider: #263a63;
    --white: #ffffff;
  }
  * { box-sizing: border-box; margin: 0; padding: 0; }
  html, body { width: 1200px; height: 900px; overflow: hidden; }
  body {
    background: var(--page);
    font-family: "Open Sans", Arial, sans-serif;
    position: relative;
  }
  .card {
    position: absolute;
    left: 320px;
    width: 560px;
    height: 340px;
    border-radius: 4px;
    overflow: hidden;
    box-shadow: 0 10px 30px rgba(20, 40, 70, 0.18);
  }
  /* Front */
  .card-front { top: 60px; display: flex; }
  .front-logo-panel {
    width: 250px;
    background: var(--white);
    display: flex;
    align-items: center;
    justify-content: center;
    gap: 10px;
  }
  .front-divider { width: 8px; background: var(--divider); }
  .front-details {
    flex: 1;
    background: linear-gradient(135deg, var(--brand-blue) 0%, var(--brand-mid) 55%, var(--brand-light) 100%);
    color: var(--white);
    text-align: right;
    padding: 30px 26px 0 20px;
  }
  .holder-name { font-weight: 700; font-size: 17px; }
  .holder-role { font-size: 12.5px; margin-top: 4px; }
  .address { font-size: 12.5px; line-height: 1.4; margin-top: 22px; }
  .contact-list { list-style: none; margin-top: 16px; font-size: 13px; line-height: 1.55; }
  .contact-list li { display: flex; justify-content: flex-end; align-items: center; gap: 8px; }
  .contact-list .no-icon { padding-right: 22px; }
  .contact-icon {
    width: 14px; height: 14px;
    border-radius: 2px;
    background: rgba(255, 255, 255, 0.25);
    display: inline-flex; align-items: center; justify-content: center;
  }
  /* Logo stand-in */
  .brand-dot {
    width: 26px; height: 26px; border-radius: 50%;
    background: var(--brand-blue);
  }
  .brand-name {
    font-weight: 700;
    font-size: 30px;
    letter-spacing: 2px;
    color: var(--navy);
  }
  /* Back */
  .card-back {
    top: 480px;
    background: linear-gradient(200deg, var(--brand-blue) 0%, var(--brand-mid) 50%, var(--brand-light) 100%);
  }
  .world-map-area {
    position: absolute;
    left: 60px; top: 40px;
    width: 440px; height: 190px;
    border-radius: 40px;
    background: radial-gradient(ellipse at center, rgba(3, 60, 130, 0.35), rgba(3, 60, 130, 0));
  }
  .back-logo {
    position: absolute;
    left: 0; right: 0; top: 112px;
    display: flex; align-items: center; justify-content: center; gap: 12px;
  }
  .back-logo .brand-dot { width: 40px; height: 40px; background: var(--brand-pale); }
  .back-logo .brand-name { font-size: 42px; }
  .back-web {
    position: absolute;
    left: 0; right: 0; bottom: 58px;
    text-align: center;
    color: var(--white);
    font-size: 17px;
    letter-spacing: 0.5px;
  }
</style>
</head>
<body>

<section class="card card-front" aria-label="Business card front">
  <div class="front-logo-panel">
    <span class="brand-dot"></span>
    <span class="brand-name">LUVON</span>
  </div>
  <div class="front-divider"></div>
  <div class="front-details">
    <p class="holder-name">Emre Toksoy</p>
    <p class="holder-role">Managing Director</p>
    <p class="address">4712 Sokak No: 9<br>KBSE Yenikent IZMIR TURKEY</p>
    <ul class="contact-list">
      <li>+902324815263
        <span class="contact-icon"><svg width="10" height="10" viewBox="0 0 10 10"><path d="M2 1 L4 1 L4.6 3 L3.6 3.8 Q4.6 5.6 6.2 6.4 L7 5.4 L9 6 L9 8 Q5 9 1 2 Z" fill="#fff"/></svg></span>
      </li>
      <li>+902324815269
        <span class="contact-icon"><svg width="10" height="10" viewBox="0 0 10 10"><rect x="1" y="4" width="8" height="5" fill="#fff"/><rect x="3" y="1" width="4" height="3" fill="none" stroke="#fff"/></svg></span>
      </li>
      <li>info@luvon.com
        <span class="contact-icon"><svg width="10" height="10" viewBox="0 0 10 10"><rect x="1" y="2.5" width="8" height="5.5" fill="none" stroke="#fff"/><path d="M1 2.5 L5 6 L9 2.5" fill="none" stroke="#fff"/></svg></span>
      </li>
      <li>www.luvon.com.tr
        <span class="contact-icon"><svg width="10" height="10" viewBox="0 0 10 10"><circle cx="5" cy="5" r="3.8" fill="none" stroke="#fff"/><path d="M1.2 5 H8.8 M5 1.2 V8.8" stroke="#fff" stroke-width="0.8"/></svg></span>
      </li>
    </ul>
  </div>
</section>

<section class="card card-back" aria-label="Business card back">
  <div class="world-map-area" role="img" aria-label="Dotted world map in darker blue"></div>
  <div class="back-logo">
    <span class="brand-dot"></span>
    <span class="brand-name">LUVON</span>
  </div>
  <p class="back-web">www.luvon.com.tr</p>
</section>

</body>
</html>
```